Business card for Full Stable Care Vandorpe

I would like to have me designed an professional business card with my existing logo for my company called : full stable care vandorpe gcv.
I prefer a two sided business card with on the back side only the horses head and the website : fscvandorpe-example.eu
Only one colour shouldbe all right.
The logo must appear in a nic professional way on the business card.

Other suggestion are welcome.

All copy wrights must be released by the designer after we have selected a final design.

Target Market(s)

Equestrian businesses

Industry/Entity Type

Business

Contact Information for Business Card

Laurent Vandorpe
Title: zaakvoerder
Full Stable Care Vandorpe GCV
Molkenweg 47
B - 2820 Bonheiden
België
Phone: + 32 491 68 27 04
Mail: laurent@fscvandorpe-example.eu

Font styles to use
Serif

Requirements
Must have
• My own logo
• See attached files
• Website: fscvandorpe-example.eu

```html
<!DOCTYPE html>
<html lang="en">
<head>
<meta charset="utf-8">
<title>Full Stable Care Vandorpe — Business Card</title>
<link rel="stylesheet" href="https://fonts.googleapis.com/css2?family=Open+Sans:wght@400;700&display=swap">
<style>
  :root {
    --ink: #2b2b2b;
    --ink-soft: #555555;
    --paper: #ffffff;
    --stage: #e9e9e9;
    --band: #3a3a3a;
    --band-light: #6a6a6a;
    --rule: #cfcfcf;
  }
  * { box-sizing: border-box; margin: 0; padding: 0; }
  html, body {
    width: 1200px; height: 900px; overflow: hidden;
    background: var(--stage);
    font-family: "Open Sans", Arial, sans-serif;
    color: var(--ink);
  }
  .sheet {
    position: relative; width: 1200px; height: 900px;
  }
  .card {
    position: absolute; left: 280px; width: 640px; height: 400px;
    background: var(--paper);
    box-shadow: 0 6px 18px rgba(0,0,0,0.18);
    overflow: hidden;
  }
  .card--back { top: 30px; }
  .card--front { top: 468px; }

  /* back side */
  .back-mark {
    position: absolute; left: 0; right: 0; top: 130px;
    text-align: center;
    font-weight: 700; font-size: 30px; letter-spacing: 1px;
    color: var(--ink);
  }
  .back-mark__dot {
    display: block; width: 48px; height: 48px; margin: 0 auto 18px;
    border-radius: 50%; background: var(--ink);
  }
  .back-web {
    position: absolute; right: 36px; bottom: 34px;
    font-size: 17px; color: var(--ink);
  }

  /* front side */
  .brand {
    position: absolute; left: 0; right: 0; top: 58px;
    text-align: center;
    font-weight: 700; font-size: 36px; letter-spacing: 0.5px;
    color: var(--ink);
  }
  .person {
    position: absolute; left: 56px; top: 212px;
  }
  .person__name { font-weight: 700; font-size: 24px; line-height: 1.1; }
  .person__title { font-size: 19px; color: var(--ink-soft); }
  .divider {
    position: absolute; left: 345px; top: 210px; width: 1px; height: 92px;
    background: linear-gradient(var(--paper), var(--rule), var(--paper));
  }
  .contacts {
    position: absolute; left: 368px; top: 212px; list-style: none;
    font-size: 16px; color: var(--ink);
  }
  .contacts li { display: flex; align-items: center; gap: 10px; height: 29px; }
  .contacts svg { width: 15px; height: 15px; flex: none; }
  .contacts .at { width: 15px; font-weight: 700; text-align: center; font-size: 16px; }
  .band { position: absolute; left: 0; bottom: 0; width: 640px; height: 70px; }
</style>
</head>
<body>
<main class="sheet">

  <section class="card card--back" aria-label="Card back">
    <div class="back-mark"><span class="back-mark__dot"></span>Full Stable Care Vandorpe</div>
    <p class="back-web">fscvandorpe-example.eu</p>
  </section>

  <section class="card card--front" aria-label="Card front">
    <h1 class="brand">Full Stable Care Vandorpe</h1>

    <div class="person">
      <p class="person__name">Laurent Vandorpe</p>
      <p class="person__title">Manager</p>
    </div>

    <div class="divider"></div>

    <ul class="contacts">
      <li>
        <svg viewBox="0 0 24 24" aria-hidden="true"><path fill="#2b2b2b" d="M6.6 10.8a15.1 15.1 0 0 0 6.6 6.6l2.2-2.2c.3-.3.7-.4 1-.2 1.1.4 2.3.6 3.6.6.6 0 1 .4 1 1V20c0 .6-.4 1-1 1A17 17 0 0 1 3 4c0-.6.4-1 1-1h3.5c.6 0 1 .4 1 1 0 1.3.2 2.5.6 3.6.1.3 0 .7-.2 1z"/></svg>
        <span>32 491 68 27 04</span>
      </li>
      <li>
        <svg viewBox="0 0 24 24" aria-hidden="true" fill="none" stroke="#2b2b2b" stroke-width="1.8"><circle cx="12" cy="12" r="9"/><path d="M3 12h18M12 3c3 3 3 15 0 18M12 3c-3 3-3 15 0 18"/></svg>
        <span>fscvandorpe-example.eu</span>
      </li>
      <li>
        <span class="at">@</span>
        <span>laurent@fscvandorpe-example.eu</span>
      </li>
    </ul>

    <svg class="band" viewBox="0 0 640 70" preserveAspectRatio="none" aria-hidden="true">
      <path d="M0 44 H640 V70 H0 Z" fill="var(--band)"/>
      <path d="M470 70 C500 40 540 28 640 24 V70 Z" fill="var(--band)"/>
      <path d="M440 70 C480 44 530 36 640 36" fill="none" stroke="var(--paper)" stroke-width="5"/>
      <path d="M0 44 H470" stroke="var(--band-light)" stroke-width="2"/>
    </svg>
  </section>

</main>
</body>
</html>
```